Creative Agency Showcase/Profile

Looking for a impactful, clean design to showcase our best works.

Our events company: www.brightkiteevents.com.sg

We have a clean and impactful look which we want to maintain. Looking at how we can best showcase our works/events to new customers who we want to do business with.

Actual photos will be provided once appointed.

Target Market(s)

Corporates, New Customers

Font styles to use
Sans Serif

Colors
ec1f27
0592cd
f78f20
6b439b
ffffff

Requirements
Must have
• Key Tagline:
• BREAKING NEW GROUND
• To be presented on a 16:9 Landscape format (prefably editable in KEYNOTE in the future)
• Total should be at least 8-10 pages including a COVER PAGE and CONTACT US PAGE.
Nice to have
• Some secondary captions/by lines.
• Must include event pictures.
• Hoping to have one picture per slide.
• Please use stock images at least 8-10 for now.

```html
<!DOCTYPE html>
<html lang="en">
<head>
<meta charset="utf-8">
<title>Lumenfield Events — Profile</title>
<link href="https://fonts.googleapis.com/css2?family=Montserrat:ital,wght@0,400;0,600;0,700;0,800;1,700;1,800&display=swap" rel="stylesheet">
<style>
:root{
  --blue:#1b6fc8;
  --dark:#3f3f41;
  --light:#f6f6f7;
  --white:#ffffff;
  --ink:#111111;
}
*{margin:0;padding:0;box-sizing:border-box}
html,body{width:711px;height:1200px;overflow:hidden;background:var(--white)}
body{font-family:"Montserrat",Arial,sans-serif;color:var(--blue);position:relative}
.box{position:absolute}
.photo{position:absolute}
.light{background:var(--light)}
.dark{background:var(--dark);color:var(--white)}
.blueblock{background:var(--blue);color:var(--white)}
.h-bold{font-weight:700;line-height:1.15;letter-spacing:-0.2px}
.h-thin{font-weight:400;letter-spacing:-0.3px}
.body{font-size:3.9px;line-height:1.85;font-weight:600}
.right{text-align:right}
.center{text-align:center}
.justify{text-align:justify}
.btn{position:absolute;background:var(--blue);color:var(--white);font-weight:800;font-style:italic;font-size:7.5px;padding:1.5px 3px;border:0.6px solid #0d4f99;white-space:nowrap}
.service{position:absolute;right:0;text-align:right}
.service h4{font-size:5.2px;font-weight:700;color:var(--blue)}
.service p{font-size:2.8px;line-height:1.5;color:#8c8c8c;font-weight:600}
.tick{position:absolute;width:10px;height:10px}
.spec h3{font-size:7.4px;font-weight:700;line-height:1.25;color:var(--white);letter-spacing:-0.3px;white-space:nowrap}
.spec p{font-size:3.4px;line-height:1.6;font-weight:600;margin:4px 0 14px}
.band{position:absolute;background:var(--blue);height:22px}
.avatar{position:absolute;width:52px;height:52px;border-radius:50%;border:1.5px solid #c9d3de;background:radial-gradient(circle at 50% 40%,#f2f2f2,#dcdcdc)}
.teams-title{position:absolute;font-weight:800;font-style:italic;font-size:14px;color:var(--blue);letter-spacing:-0.3px}
.teams-title span{color:#444}
</style>
</head>
<body>

<!-- Row 1 -->
<div class="photo" style="left:0;top:0;width:176px;height:200px;background:linear-gradient(160deg,#7a2a6a,#d4502a 40%,#2a0f1a 80%)" role="img" aria-label="Concert crowd filming stage lights on a phone"></div>
<section class="box" style="left:176px;top:0;width:359px;height:200px;background:var(--white)">
  <h1 class="box h-bold right" style="left:40px;width:128px;top:48px;font-size:13.5px">Breaking<br>New Ground</h1>
  <p class="box body center" style="left:45px;width:125px;top:92px">A full-fledged events company offering the full range of high-quality services, we have mapped an impressive network of partners and solutions so as to bring to you competitively priced event packages with no third party fees and charges since we manage our own in-house event solutions ranging from design &amp; print, audio visual and even our own staging and logistics!</p>
  <div class="btn" style="left:46px;top:153px">Check it Out</div>
  <h2 class="box h-bold right" style="left:210px;width:139px;top:42px;font-size:13.5px">We Are<br><span style="color:var(--ink)">Lumenfield</span></h2>
  <p class="box body center" style="left:217px;width:132px;top:89px">A full-fledged events company offering the full range of high-quality services, we have mapped an impressive network of partners and solutions so as to bring to you competitively priced event packages with no third party fees and charges since we manage our own in-house event solutions ranging from design &amp; print, audio visual and even our own staging and logistics!</p>
</section>
<div class="photo" style="left:535px;top:0;width:176px;height:200px;background:linear-gradient(180deg,#cfcfd2,#7d7f86 45%,#3a3a40)" role="img" aria-label="Seated workshop audience under silver balloons"></div>

<!-- Row 2 -->
<section class="box light" style="left:0;top:200px;width:119px;height:200px">
  <div class="service" style="right:35px;top:47px;width:80px"><h4>DESIGN TEAM</h4><p>The design team will see to your specific needs for all kinds of creatives! From invites to backdrop to customised props design</p></div>
  <div class="service" style="right:35px;top:75px;width:80px"><h4>ADMIN FINANCE</h4><p>Handling all our accounts, legal and admin, you can leave all the knitty gritty to our trusty team and focus on what really needs your attention</p></div>
  <div class="service" style="right:35px;top:106px;width:80px"><h4>OPERATION</h4><p>Our men on the ground will handle all the operational needs of your event on the actual day</p></div>
  <div class="service" style="right:35px;top:134px;width:80px"><h4>AUDIO VISUAL</h4><p>Our AV team is made of specialised audio and lighting technician managed by show producers</p></div>
  <svg class="tick" style="left:90px;top:47px" viewBox="0 0 10 10"><circle cx="5" cy="5" r="5" fill="#1b6fc8"/><path d="M2.6 5.2l1.7 1.6 3.2-3.4" stroke="#fff" stroke-width="1.1" fill="none"/></svg>
  <svg class="tick" style="left:90px;top:75px" viewBox="0 0 10 10"><circle cx="5" cy="5" r="5" fill="#1b6fc8"/><path d="M2.6 5.2l1.7 1.6 3.2-3.4" stroke="#fff" stroke-width="1.1" fill="none"/></svg>
  <svg class="tick" style="left:90px;top:106px" viewBox="0 0 10 10"><circle cx="5" cy="5" r="5" fill="#1b6fc8"/><path d="M2.6 5.2l1.7 1.6 3.2-3.4" stroke="#fff" stroke-width="1.1" fill="none"/></svg>
  <svg class="tick" style="left:90px;top:134px" viewBox="0 0 10 10"><circle cx="5" cy="5" r="5" fill="#1b6fc8"/><path d="M2.6 5.2l1.7 1.6 3.2-3.4" stroke="#fff" stroke-width="1.1" fill="none"/></svg>
</section>
<div class="photo" style="left:119px;top:200px;width:99px;height:200px;background:linear-gradient(150deg,#2b3a44,#17323f 45%,#7a3a2a 80%,#c0604a)" role="img" aria-label="Hands on a backlit keyboard"></div>
<section class="box dark" style="left:218px;top:200px;width:137px;height:200px">
  <h2 class="box h-bold right" style="right:22px;top:58px;font-size:13.5px">Our<br>Team Service</h2>
  <p class="box body center" style="left:12px;width:112px;top:104px">The Lumenfield team is made of professional experience managers that will see your event through to a successful conclusion. Please contact our experienced managers to see how we can help you:</p>
</section>
<div class="photo" style="left:355px;top:200px;width:100px;height:200px;background:linear-gradient(160deg,#2f3d55,#a07f70 50%,#6b2b35)" role="img" aria-label="Speaker gesturing with open hand"></div>
<section class="box dark spec" style="left:455px;top:200px;width:116px;height:200px;padding:30px 15px 0 18px;text-align:right">
  <h3>Event Specialisations</h3>
  <p style="text-align:left">Lumenfield specialises in a variety of events. Click the link below to see the types of events we do!</p>
  <h3>Events Management<br>Services</h3>
  <p style="text-align:left">Lumenfield specialises in a variety of events. Click the link below to see the types of events we do!</p>
  <h3>Audio &amp; Visual<br>Support</h3>
  <p style="text-align:left">Lumenfield specialises in a variety of events. Click the link below to see the types of events we do!</p>
</section>
<section class="box" style="left:571px;top:200px;width:140px;height:200px">
  <h2 class="box h-bold right" style="right:17px;top:44px;font-size:13.5px">Our<br>Services</h2>
  <p class="box body right" style="right:17px;width:105px;top:82px;font-size:3.6px">From the initial stages of creating and planning to organising and management and eventually to delivering endless memorable event experiences, we do it all.o more than just create event experiences. We recreate and redefine event experiences through 360 event solutions. Just imagine a sensory experience that colours your brand; where your message comes alive. Lumenfield lives and breathes everything that you can associate events with.</p>
</section>

<!-- Row 3 -->
<section class="box" style="left:0;top:400px;width:110px;height:100px">
  <p class="box body justify" style="left:19px;width:73px;top:28px;font-size:3.6px">Lorem Isum Aliquam varius adipiscing tempor. Vivamus id ipsum sit amet massa consectetur porta. Class aptent taciti sociosqu ad litora torquent per conubia nostra, per inceptos himenaeos.</p>
</section>
<div class="photo" style="left:110px;top:400px;width:109px;height:100px;background:linear-gradient(180deg,#7d9a4e,#5f7c3a 50%,#c0543a)" role="img" aria-label="Cycling peloton racing on a country road"></div>
<div class="photo" style="left:0;top:500px;width:110px;height:100px;background:linear-gradient(170deg,#b8c6d0,#3a4654 55%,#1f2a3a)" role="img" aria-label="Cyclists sprinting past spectators"></div>
<section class="box light" style="left:110px;top:500px;width:109px;height:100px">
  <h3 class="box h-thin center" style="left:0;width:109px;top:31px;font-size:9.5px">Special Events</h3>
  <p class="box body center" style="left:9px;width:91px;top:50px;font-size:3.3px">Lorem ipsum dolor sit amet, lacus nulla ac netus nibh aliquet, porttitor ligula justo libero vivamus porttitor dolor, conubia mollit. Sapien nam suspendisse, tincidunt eget ante tincidunt, eros in auctor</p>
</section>
<section class="box" style="left:219px;top:400px;width:136px;height:200px">
  <h2 class="box h-bold right" style="right:19px;top:52px;font-size:13.5px">Special<br>Events</h2>
  <p class="box body right" style="right:19px;width:85px;top:95px;font-size:3.6px">Lorem Isum Aliquam varius adipiscing tempor. Vivamus id ipsum sit amet massa consectetur porta. Class aptent taciti sociosqu ad litora torquent per conubia nostra, per inceptos himenaeos.</p>
  <div class="btn" style="right:19px;top:160px">Check it Out</div>
</section>
<section class="box light" style="left:355px;top:400px;width:110px;height:100px">
  <h3 class="box h-thin center" style="left:0;width:110px;top:33px;font-size:9.5px">Special Events</h3>
  <p class="box body center" style="left:11px;width:90px;top:52px;font-size:3.3px">Lorem ipsum dolor sit amet, lacus nulla ac netus nibh aliquet, porttitor ligula justo libero vivamus porttitor dolor, conubia mollit. Sapien nam suspendisse, tincidunt eget ante tincidunt, eros in auctor</p>
</section>
<div class="photo" style="left:465px;top:400px;width:109px;height:100px;background:linear-gradient(180deg,#d8d8d8,#4a4a4a 45%,#d8432e 80%)" role="img" aria-label="Weightlifter bench pressing on red gym floor"></div>
<div class="photo" style="left:355px;top:500px;width:110px;height:100px;background:linear-gradient(180deg,#9a9a9a,#e08a2a 50%,#2a7ac8)" role="img" aria-label="Group in orange shirts posing on blue mat"></div>
<section class="box light" style="left:465px;top:500px;width:109px;height:100px">
  <p class="box body justify" style="left:18px;width:73px;top:31px;font-size:3.6px">Lorem Isum Aliquam varius adipiscing tempor. Vivamus id ipsum sit amet massa consectetur porta. Class aptent taciti sociosqu ad litora torquent per conubia nostra, per inceptos himenaeos.</p>
</section>
<section class="box" style="left:574px;top:400px;width:137px;height:200px">
  <h2 class="box h-bold right" style="right:19px;top:52px;font-size:13.5px">Special<br>Events</h2>
  <p class="box body right" style="right:19px;width:85px;top:95px;font-size:3.6px">Lorem Isum Aliquam varius adipiscing tempor. Vivamus id ipsum sit amet massa consectetur porta. Class aptent taciti sociosqu ad litora torquent per conubia nostra, per inceptos himenaeos.</p>
  <div class="btn" style="right:19px;top:160px">Check it Out</div>
</section>

<!-- Row 4 -->
<section class="box" style="left:0;top:600px;width:176px;height:100px">
  <h3 class="box h-thin center" style="left:0;width:176px;top:31px;font-size:11.5px">Launch &amp; Activation</h3>
  <p class="box body center" style="left:42px;width:94px;top:52px;font-size:3.3px">Lorem ipsum dolor sit amet, lacus nulla ac netus nibh aliquet, porttitor ligula justo libero vivamus porttitor dolor, conubia mollit. Sapien nam suspendisse, tincidunt eget ante tincidunt, eros in auctor</p>
</section>
<div class="photo" style="left:176px;top:600px;width:179px;height:100px;background:linear-gradient(170deg,#9fb3bf,#dfe8ee 45%,#2a2a30 75%)" role="img" aria-label="Officials pressing a button at an opening ceremony"></div>
<div class="photo" style="left:0;top:700px;width:176px;height:100px;background:linear-gradient(160deg,#dcdcdc,#7bb7d8 40%,#d24f7a 70%,#5aa65a)" role="img" aria-label="Guests under falling confetti at a launch"></div>
<section class="box" style="left:176px;top:700px;width:179px;height:100px">
  <h3 class="box h-thin center" style="left:0;width:179px;top:30px;font-size:11.5px">Launch &amp; Activation</h3>
  <p class="box body center" style="left:44px;width:94px;top:51px;font-size:3.3px">Lorem ipsum dolor sit amet, lacus nulla ac netus nibh aliquet, porttitor ligula justo libero vivamus porttitor dolor, conubia mollit. Sapien nam suspendisse, tincidunt eget ante tincidunt, eros in auctor</p>
</section>
<div class="photo" style="left:384px;top:609px;width:80px;height:113px;background:linear-gradient(180deg,#e6e8ea,#9aa0a8 40%,#3a3f4a)" role="img" aria-label="Award winners posing in a row"></div>
<h2 class="box h-bold" style="left:386px;top:740px;font-size:13.5px">Award &amp;<br>Ceremony</h2>
<section class="box dark" style="left:481px;top:609px;width:101px;height:179px">
  <h3 class="box h-thin center" style="left:0;width:101px;top:69px;font-size:11px;color:var(--white)">Award Info</h3>
  <p class="box body center" style="left:8px;width:85px;top:93px;font-size:3px">Lorem ipsum dolor sit amet, lacus nulla ac netus nibh aliquet, porttitor ligula justo libero vivamus porttitor dolor, conubia mollit. Sapien nam suspendisse, tincidunt eget ante tincidunt, eros in auctor</p>
</section>
<p class="box body justify" style="left:594px;width:79px;top:627px;font-size:3.3px">Lorem ipsum dolor sit amet, lacus nulla ac netus nibh aliquet, porttitor ligula justo libero vivamus porttitor dolor, conubia mollit. Sapien nam suspendisse, tincidunt eget ante tincidunt, eros in auctor</p>
<div class="photo" style="left:593px;top:676px;width:80px;height:112px;background:linear-gradient(180deg,#2a2418,#8a7240 40%,#3a2a2a 70%,#8a1f1f)" role="img" aria-label="Award stage with screen and red carpet"></div>

<!-- Row 5 -->
<section class="box" style="left:0;top:800px;width:355px;height:200px">
  <div class="box" style="left:0;top:120px;width:355px;height:80px;background:var(--dark)"></div>
  <div class="photo" style="left:15px;top:16px;width:124px;height:165px;background:linear-gradient(160deg,#5a1a1a,#e6e6e6 45%,#d94f7a 70%,#e8e0d0)" role="img" aria-label="Dancer with pink ribbon at an anniversary dinner"></div>
  <div class="box blueblock" style="left:139px;top:16px;width:204px;height:165px"></div>
  <div class="photo" style="left:103px;top:34px;width:96px;height:128px;background:linear-gradient(180deg,#6a6458,#2a2a2a 55%,#e8e6e0)" role="img" aria-label="Guest applauding at a banquet table"></div>
  <h2 class="box h-bold right" style="right:36px;top:41px;font-size:13.5px;color:var(--white)">Dancing &amp;<br>Dinner</h2>
  <p class="box body right" style="right:36px;width:85px;top:101px;color:var(--white);font-size:3.6px">Lorem Isum Aliquam varius adipiscing tempor. Vivamus id ipsum sit amet massa consectetur porta. Class aptent taciti sociosqu ad litora torquent per conubia nostra, per inceptos himenaeos.</p>
</section>
<section class="box" style="left:355px;top:800px;width:356px;height:200px">
  <h2 class="teams-title" style="left:143px;top:30px">Our <span>Teams</span></h2>
  <div class="band" style="left:0;top:102px;width:356px"></div>
  <div class="avatar" style="left:46px;top:68px" role="img" aria-label="Team member portrait"></div>
  <div class="avatar" style="left:151px;top:68px" role="img" aria-label="Team member portrait"></div>
  <div class="avatar" style="left:256px;top:68px" role="img" aria-label="Team member portrait"></div>
  <p class="box body justify" style="left:29px;width:141px;top:151px;font-size:3.5px">A wonderful serenity has taken possession of my entire soul, like these sweet mornings of spring which I enjoy with my whole heart. I am alone, and feel the charm of existence in this spot, which was created for the bliss of souls like mine. I am so happy, my dear friend.</p>
  <h3 class="box h-thin" style="left:186px;top:155px;font-size:11px">Team Info</h3>
  <p class="box body justify" style="left:251px;width:84px;top:151px;font-size:3.2px">Lorem ipsum dolor sit amet, lacus nulla ac netus nibh aliquet, porttitor ligula justo libero vivamus porttitor dolor, conubia mollit. Sapien nam</p>
</section>

<!-- Row 6 -->
<section class="box" style="left:0;top:1000px;width:355px;height:200px">
  <h2 class="teams-title" style="left:143px;top:30px">Our <span>Teams</span></h2>
  <div class="band" style="left:0;top:102px;width:355px"></div>
  <div class="avatar" style="left:40px;top:67px" role="img" aria-label="Team member portrait"></div>
  <div class="avatar" style="left:115px;top:67px" role="img" aria-label="Team member portrait"></div>
  <div class="avatar" style="left:189px;top:67px" role="img" aria-label="Team member portrait"></div>
  <div class="avatar" style="left:264px;top:67px" role="img" aria-label="Team member portrait"></div>
  <p class="box body justify" style="left:29px;width:141px;top:151px;font-size:3.5px">A wonderful serenity has taken possession of my entire soul, like these sweet mornings of spring which I enjoy with my whole heart. I am alone, and feel the charm of existence in this spot, which was created for the bliss of souls like mine. I am so happy, my dear friend.</p>
  <h3 class="box h-thin" style="left:186px;top:155px;font-size:11px">Team Info</h3>
  <p class="box body justify" style="left:251px;width:84px;top:151px;font-size:3.2px">Lorem ipsum dolor sit amet, lacus nulla ac netus nibh aliquet, porttitor ligula justo libero vivamus porttitor dolor, conubia mollit. Sapien nam</p>
</section>
<section class="box" style="left:355px;top:1000px;width:356px;height:200px">
  <div class="box light" style="left:0;top:0;width:113px;height:200px"></div>
  <div class="photo" style="left:27px;top:19px;width:119px;height:168px;border-radius:5px;background:linear-gradient(180deg,#1a1a1a,#5a4a3a 30%,#2a2a2a 60%,#b65a3a 80%,#1a1a1a)" role="img" aria-label="Tablet showing a laptop on a wooden desk"></div>
  <h2 class="box h-bold right" style="right:38px;top:39px;font-size:13.5px">Get In<br>Touch</h2>
  <p class="box body right" style="right:38px;width:95px;top:75px;font-size:4px">Have any enquiries or desires? Share it with us!</p>
  <p class="box body right" style="right:38px;top:95px;font-size:3.5px">Address:</p>
  <p class="box right" style="right:38px;top:106px;font-size:5.8px;line-height:1.25;font-weight:400">18 Harbour Lane<br>#04-12, Meridian<br>Singapore 534210</p>
  <p class="box body right" style="right:38px;top:135px;font-size:3.2px">Tel.: +65 6310 2245 Fax: +65 6310 2246</p>
  <p class="box body right" style="right:38px;top:147px;font-size:3.2px">Email : contact@lumenfieldevents.com.sg</p>
</section>

</body>
</html>
```